Travel Activities - Tours, sightseeing tours, activities & things to do website design

We need a web design that covers Tours, sightseeing tours, activities and things to do in the travel industry. Need to be a simple design with good SEO technical structure and conversion optimised design.
Inspirations
Similar site - https://www.wandoro.com/London/d512-ttd?pub=KRT8VX_4_7
Design and layout - https://www.stayplumo.com.au/europe-294/hotel
Colours - please suggest ( prefer happy energetic colours )
Pages
1. Home page design
2. Individual tour or activity page design
Target Market(s)
Independent travellers who want to plan the holiday by themselfs.
Industry/Entity Type
Travel Industry
Number of Pages Required
2 page
Colors
Designer to choose colors to be used in the design.
Requirements
Must have
- Pages
- 1. Home page design
- 2. Individual tour or activity page design
- SEO
- H1 tags
- Text Descriptions
- Internal linking to other tours activities

```html
<!DOCTYPE html>
<html lang="en">
<head>
<meta charset="utf-8">
<title>Wayfarer Desk – Tours, Tickets, Activities &amp; Things To Do in London</title>
<link href="https://fonts.googleapis.com/css2?family=Roboto:wght@400;500;700&display=swap" rel="stylesheet">
<style>
:root{
  --blue:#2f82c8;
  --blue-dark:#2571b3;
  --orange:#ff8a00;
  --ink:#222;
  --muted:#777;
  --line:#e2e2e2;
  --bg:#f4f4f4;
  --footer:#161616;
  --red:#e53935;
}
*{box-sizing:border-box;margin:0;padding:0}
html,body{width:1200px;height:3629px;overflow:hidden}
body{font-family:"Roboto",Arial,sans-serif;color:var(--ink);background:#fff;position:relative}
.abs{position:absolute}
a{color:inherit;text-decoration:none}

/* header */
.site-header{position:absolute;left:0;top:0;width:1200px;height:213px;background:var(--blue)}
.topbar{position:absolute;left:99px;right:99px;top:0;height:29px;font-size:13px;color:#fff;font-weight:500;display:flex;align-items:center}
.topbar .right{margin-left:auto;display:flex;gap:26px;align-items:center;height:100%}
.cart{background:var(--orange);height:29px;padding:0 14px;display:flex;align-items:center}
.brand{position:absolute;left:99px;top:58px;font-size:26px;font-weight:700;color:#fff;letter-spacing:.3px}
.search{position:absolute;left:617px;top:53px;width:484px;height:44px;display:flex}
.search .field{flex:1;background:#fff;display:flex;align-items:center;padding-left:14px}
.search button{width:97px;border:0;background:var(--blue-dark);color:#fff;font:500 15px "Roboto",sans-serif}
.header-rule{position:absolute;left:617px;width:484px;top:113px;height:1px;background:rgba(255,255,255,.35)}
.loc{position:absolute;top:135px;height:46px;border:1px solid rgba(255,255,255,.6);background:var(--blue);color:#fff;font-size:14px;display:flex;align-items:center;padding-left:18px;gap:8px}
.go{position:absolute;left:944px;top:135px;width:60px;height:46px;background:var(--orange);color:#fff;font-weight:700;font-size:15px;display:flex;align-items:center;justify-content:center}

/* breadcrumb */
.breadcrumb{position:absolute;left:99px;top:226px;font-size:13px;font-weight:700}
.breadcrumb .current{color:var(--orange)}
.share{position:absolute;right:99px;top:223px;display:flex;gap:8px;align-items:center;font-size:11px;color:var(--muted)}
.share span.btn{display:inline-block;width:52px;height:20px;border-radius:2px}
.share span.sq{width:26px}
.rule{position:absolute;left:99px;width:1002px;height:1px;background:var(--line)}

/* sidebar */
.side-head{position:absolute;left:99px;width:206px;height:42px;background:var(--blue);color:#fff;font-weight:700;font-size:16px;display:flex;align-items:center;padding:0 16px;justify-content:space-between;text-transform:uppercase}
.side-head.active{background:var(--orange)}
.tours-box{position:absolute;left:99px;top:300px;width:206px;height:177px;border:1px solid var(--line)}
.tours-box .label{position:absolute;left:10px;top:58px;font-size:13px}
.date{position:absolute;left:10px;width:184px;height:30px;border:1px solid #ccc;font-size:12px;color:#999;display:flex;align-items:center;padding:0 10px;justify-content:space-between}
.newsletter{position:absolute;left:99px;top:765px;width:206px;height:162px;border:2px solid var(--line);padding:16px 14px}
.newsletter h3{font-size:17px;font-weight:700}
.newsletter .email{margin-top:16px;width:178px;height:34px;border:1px solid #bbb;font-size:12px;color:#666;display:flex;align-items:center;padding-left:10px}
.newsletter .signup{margin-top:16px;width:80px;height:32px;background:var(--blue);color:#fff;font-size:12px;font-weight:700;border-radius:3px;display:flex;align-items:center;justify-content:center}

/* main */
.hero{position:absolute;left:346px;top:300px;width:755px;height:184px;background:linear-gradient(180deg,#2a4a7c 0%,#6a6f8a 45%,#c88a55 75%,#1d2a3c 100%)}
.hero h1{position:absolute;left:36px;top:70px;font-size:33px;font-weight:500;color:#fff}
.results{position:absolute;left:346px;top:518px;font-size:15px;color:#555}
.sort{position:absolute;left:845px;top:518px;font-size:13px;font-weight:700}
.sort-select{position:absolute;left:922px;top:507px;width:179px;height:43px;border:1px solid #ccc;font-size:13px;color:#666;display:flex;align-items:center;padding-left:14px}
.sort-select i{position:absolute;right:0;top:0;width:42px;height:41px;border-left:1px solid #ccc;display:flex;align-items:center;justify-content:center;font-style:normal}

.card{position:absolute;left:346px;width:755px;height:183px;border:1px solid var(--line);background:#fff}
.card .photo{position:absolute;left:0;top:0;width:223px;height:181px}
.card .fav{position:absolute;left:188px;top:148px}
.card h2{position:absolute;left:252px;top:30px;width:240px;font-size:16px;font-weight:700;line-height:23px}
.card .stars{position:absolute;left:252px;top:85px;font-size:12px;color:#555;display:flex;gap:6px;align-items:center}
.card .stars b{color:#f5a623;font-weight:400;letter-spacing:1px}
.card .meta{position:absolute;left:252px;font-size:13px;color:#555;display:flex;gap:8px;align-items:center}
.card .divider{position:absolute;left:500px;top:22px;width:1px;height:138px;background:var(--line)}
.card .pick{position:absolute;left:559px;top:22px;font-size:17px;font-weight:500}
.card .from{position:absolute;left:538px;top:44px;font-size:17px}
.card .from strong{color:var(--blue);font-size:31px;font-weight:700}
.card .save{position:absolute;left:538px;top:85px;font-size:17px}
.card .save s{font-weight:700}
.card .save span{color:var(--red)}
.card .deal{position:absolute;left:564px;top:115px;width:126px;height:44px;background:var(--orange);color:#fff;font-weight:700;font-size:15px;border-radius:3px;display:flex;align-items:center;justify-content:center}

.pager{position:absolute;left:346px;top:2352px;display:flex;gap:6px}
.pager span{height:24px;min-width:24px;padding:0 7px;border:1px solid #ccc;font-size:11px;display:flex;align-items:center;justify-content:center;color:#444}
.pager span.on{background:var(--orange);border-color:var(--orange);color:#fff}

.panel{position:absolute;left:346px;width:755px;border:1px solid var(--line);background:#fff}
.panel h2{position:absolute;left:30px;top:32px;font-size:30px;font-weight:500}
.arrows{position:absolute;right:28px;top:42px;display:flex;gap:6px}
.arrows span{width:24px;height:24px;border-radius:50%;background:#c8c8c8;display:flex;align-items:center;justify-content:center}
.dest{position:absolute;top:98px;width:219px;height:226px;border:1px solid var(--line)}
.dest .photo{width:217px;height:157px}
.dest .name{position:absolute;left:12px;top:172px;font-size:15px;font-weight:700}
.dest .count{position:absolute;left:12px;top:195px;font-size:13px;font-style:italic;color:#555}
.dest .price{position:absolute;right:14px;top:180px;color:var(--orange);font-weight:700;font-size:15px}

.things{position:absolute;left:40px;top:102px;display:grid;grid-template-columns:254px 225px 200px;grid-auto-flow:column;grid-template-rows:repeat(7,29px)}
.things li{list-style:none;font-size:13px;color:#555;display:flex;align-items:center;gap:10px}
.things li::before{content:"";width:12px;height:12px;border-radius:50%;background:var(--orange);box-shadow:inset 0 0 0 3px var(--orange)}

/* footer */
.site-footer{position:absolute;left:0;top:3253px;width:1200px;height:376px;background:var(--footer);color:#fff}
.foot-brand{position:absolute;left:95px;top:108px;font-size:27px;font-weight:700}
.foot-about{position:absolute;left:95px;top:158px;width:290px;font-size:12px;line-height:20px;color:#ccc}
.socials{position:absolute;left:97px;top:227px;display:flex;gap:6px}
.socials span{width:21px;height:21px;border-radius:50%}
.foot-col{position:absolute;top:78px}
.foot-col h4{font-size:18px;font-weight:700;margin-bottom:20px}
.foot-col li{list-style:none;font-size:12px;color:#ddd;height:27px}
.copyright{position:absolute;left:0;width:1200px;top:329px;text-align:center;font-size:12px;color:#bbb}
</style>
</head>
<body>

<header class="site-header">
  <div class="topbar">
    <span>USD ($) &nbsp;&nbsp;|&nbsp;&nbsp; <svg width="16" height="10" style="vertical-align:-1px"><rect width="16" height="10" fill="#2b4c9a"/><rect y="4" width="16" height="2" fill="#fff"/><rect x="7" width="2" height="10" fill="#fff"/></svg> ENGLISH &nbsp;&nbsp;|&nbsp;&nbsp; ? HELP</span>
    <div class="right">
      <span>▦ MANAGE MY BOOKING</span>
      <span>|</span>
      <span>● LOG IN / REGISTER</span>
      <span class="cart">CART (0)</span>
    </div>
  </div>
  <a class="brand" href="#">WAYFARER DESK</a>
  <div class="search">
    <div class="field"><svg width="16" height="16" viewBox="0 0 16 16"><circle cx="6.5" cy="6.5" r="5" fill="none" stroke="#333" stroke-width="2"/><line x1="10" y1="10" x2="15" y2="15" stroke="#333" stroke-width="2"/></svg></div>
    <button>SEARCH</button>
  </div>
  <div class="header-rule"></div>
  <div class="loc" style="left:191px;width:363px"><svg width="10" height="13" viewBox="0 0 10 13"><path d="M5 0a5 5 0 0 1 5 5c0 4-5 8-5 8S0 9 0 5a5 5 0 0 1 5-5z" fill="#fff"/><circle cx="5" cy="5" r="2" fill="#2f82c8"/></svg>England</div>
  <div class="loc" style="left:567px;width:364px"><svg width="10" height="13" viewBox="0 0 10 13"><path d="M5 0a5 5 0 0 1 5 5c0 4-5 8-5 8S0 9 0 5a5 5 0 0 1 5-5z" fill="#fff"/><circle cx="5" cy="5" r="2" fill="#2f82c8"/></svg>London</div>
  <div class="go">GO</div>
</header>

<nav class="breadcrumb">HOME › ENGLAND › <span class="current">LONDON</span></nav>
<div class="share">
  <span class="btn" style="background:#3b5998"></span>0
  <span class="btn" style="background:#1da1f2"></span>1
  <span class="btn sq" style="background:#dd4b39"></span>+1
</div>
<div class="rule" style="top:254px"></div>

<aside>
  <div class="tours-box">
    <span class="label">Travel Dates</span>
    <div class="date" style="top:86px">From <span>▦</span></div>
    <div class="date" style="top:126px">To <span>▦</span></div>
  </div>
  <div class="side-head active" style="top:300px">Tours <span>⌃</span></div>
  <div class="side-head" style="top:506px">Categories <span>⌄</span></div>
  <div class="side-head" style="top:569px">Specials <span>⌄</span></div>
  <div class="side-head" style="top:632px">Price Range <span>⌄</span></div>
  <div class="side-head" style="top:695px">Duration <span>⌄</span></div>
  <div class="newsletter">
    <h3>NEWSLETTER SIGN UP</h3>
    <div class="email">Email Address</div>
    <div class="signup">SIGN UP</div>
  </div>
</aside>

<main>
  <section class="hero" role="img" aria-label="London skyline with Tower Bridge at dusk">
    <h1>Tours, Tickets, Activities &amp; Things To Do</h1>
  </section>
  <p class="results">626 out of 1,099,949 hotels</p>
  <span class="sort">SORT BY:</span>
  <div class="sort-select">Most Popular<i>▾</i></div>
  <div class="rule" style="top:576px;left:346px;width:755px"></div>

  <article class="card" style="top:608px">
    <div class="photo" role="img" aria-label="Hotel with palm trees and outdoor pool" style="background:linear-gradient(180deg,#8fc2e8,#d9cdb3 55%,#2e9ec5)"></div>
    <svg class="fav" width="20" height="18" viewBox="0 0 20 18"><path d="M10 18 1.5 9.5A5 5 0 0 1 10 3a5 5 0 0 1 8.5 6.5z" fill="#e53935"/></svg>
    <h2>Nemo enim ipsam voluptem quia voluptas sitip</h2>
    <div class="stars"><b>★★★★☆</b>5042 Reviews</div>
    <div class="meta" style="top:113px"><svg width="9" height="12" viewBox="0 0 10 13"><path d="M5 0a5 5 0 0 1 5 5c0 4-5 8-5 8S0 9 0 5a5 5 0 0 1 5-5z" fill="#ff8a00"/></svg>London, United Kingdom</div>
    <div class="meta" style="top:137px"><svg width="12" height="12" viewBox="0 0 12 12"><circle cx="6" cy="6" r="5" fill="none" stroke="#ff8a00" stroke-width="1.6"/><path d="M6 3v3h2" stroke="#ff8a00" stroke-width="1.4" fill="none"/></svg>11 hours</div>
    <div class="divider"></div>
    <div class="pick">Top Insider's Pick</div>
    <div class="from">From USD $ <strong>128.61</strong></div>
    <div class="save"><s>$135.38</s> Save <span>$6.77</span></div>
    <a class="deal" href="#">VIEW DEAL</a>
  </article>

  <article class="card" style="top:823px">
    <div class="photo" role="img" aria-label="Castle on a hill under blue sky" style="background:linear-gradient(180deg,#2f78c6,#9cc3e6 45%,#6f7e4a 75%,#3a4a2a)"></div>
    <svg class="fav" width="20" height="18" viewBox="0 0 20 18"><path d="M10 18 1.5 9.5A5 5 0 0 1 10 3a5 5 0 0 1 8.5 6.5z" fill="#e53935"/></svg>
    <h2>Nemo enim ipsam voluptem quia voluptas sitip</h2>
    <div class="stars"><b>★★★★☆</b>5042 Reviews</div>
    <div class="meta" style="top:113px"><svg width="9" height="12" viewBox="0 0 10 13"><path d="M5 0a5 5 0 0 1 5 5c0 4-5 8-5 8S0 9 0 5a5 5 0 0 1 5-5z" fill="#ff8a00"/></svg>London, United Kingdom</div>
    <div class="meta" style="top:137px"><svg width="12" height="12" viewBox="0 0 12 12"><circle cx="6" cy="6" r="5" fill="none" stroke="#ff8a00" stroke-width="1.6"/><path d="M6 3v3h2" stroke="#ff8a00" stroke-width="1.4" fill="none"/></svg>11 hours</div>
    <div class="divider"></div>
    <div class="pick">Top Insider's Pick</div>
    <div class="from">From USD $ <strong>128.61</strong></div>
    <div class="save"><s>$135.38</s> Save <span>$6.77</span></div>
    <a class="deal" href="#">VIEW DEAL</a>
  </article>

  <article class="card" style="top:1038px">
    <div class="photo" role="img" aria-label="Rooftop pool overlooking city skyscrapers" style="background:linear-gradient(180deg,#e8e2d8,#b9a58e 50%,#5fa9c7 78%,#3c7d9c)"></div>
    <svg class="fav" width="20" height="18" viewBox="0 0 20 18"><path d="M10 18 1.5 9.5A5 5 0 0 1 10 3a5 5 0 0 1 8.5 6.5z" fill="#e53935"/></svg>
    <h2>Nemo enim ipsam voluptem quia voluptas sitip</h2>
    <div class="stars"><b>★★★★☆</b>5042 Reviews</div>
    <div class="meta" style="top:113px"><svg width="9" height="12" viewBox="0 0 10 13"><path d="M5 0a5 5 0 0 1 5 5c0 4-5 8-5 8S0 9 0 5a5 5 0 0 1 5-5z" fill="#ff8a00"/></svg>London, United Kingdom</div>
    <div class="meta" style="top:137px"><svg width="12" height="12" viewBox="0 0 12 12"><circle cx="6" cy="6" r="5" fill="none" stroke="#ff8a00" stroke-width="1.6"/><path d="M6 3v3h2" stroke="#ff8a00" stroke-width="1.4" fill="none"/></svg>11 hours</div>
    <div class="divider"></div>
    <div class="pick">Top Insider's Pick</div>
    <div class="from">From USD $ <strong>128.61</strong></div>
    <div class="save"><s>$135.38</s> Save <span>$6.77</span></div>
    <a class="deal" href="#">VIEW DEAL</a>
  </article>

  <article class="card" style="top:1253px">
    <div class="photo" role="img" aria-label="Lakeside palace by calm water" style="background:linear-gradient(180deg,#a9c6df,#cfb995 50%,#4d6f8f 70%,#2d4a66)"></div>
    <svg class="fav" width="20" height="18" viewBox="0 0 20 18"><path d="M10 18 1.5 9.5A5 5 0 0 1 10 3a5 5 0 0 1 8.5 6.5z" fill="#e53935"/></svg>
    <h2>Nemo enim ipsam voluptem quia voluptas sitip</h2>
    <div class="stars"><b>★★★★☆</b>5042 Reviews</div>
    <div class="meta" style="top:113px"><svg width="9" height="12" viewBox="0 0 10 13"><path d="M5 0a5 5 0 0 1 5 5c0 4-5 8-5 8S0 9 0 5a5 5 0 0 1 5-5z" fill="#ff8a00"/></svg>London, United Kingdom</div>
    <div class="meta" style="top:137px"><svg width="12" height="12" viewBox="0 0 12 12"><circle cx="6" cy="6" r="5" fill="none" stroke="#ff8a00" stroke-width="1.6"/><path d="M6 3v3h2" stroke="#ff8a00" stroke-width="1.4" fill="none"/></svg>11 hours</div>
    <div class="divider"></div>
    <div class="pick">Top Insider's Pick</div>
    <div class="from">From USD $ <strong>128.61</strong></div>
    <div class="save"><s>$135.38</s> Save <span>$6.77</span></div>
    <a class="deal" href="#">VIEW DEAL</a>
  </article>

  <article class="card" style="top:1468px">
    <div class="photo" role="img" aria-label="Colourful waterfront town under bright sky" style="background:linear-gradient(180deg,#3a7fc9,#8dbbe3 35%,#d8a66a 60%,#2f6f8c)"></div>
    <svg class="fav" width="20" height="18" viewBox="0 0 20 18"><path d="M10 18 1.5 9.5A5 5 0 0 1 10 3a5 5 0 0 1 8.5 6.5z" fill="#e53935"/></svg>
    <h2>Nemo enim ipsam voluptem quia voluptas sitip</h2>
    <div class="stars"><b>★★★★☆</b>5042 Reviews</div>
    <div class="meta" style="top:113px"><svg width="9" height="12" viewBox="0 0 10 13"><path d="M5 0a5 5 0 0 1 5 5c0 4-5 8-5 8S0 9 0 5a5 5 0 0 1 5-5z" fill="#ff8a00"/></svg>London, United Kingdom</div>
    <div class="meta" style="top:137px"><svg width="12" height="12" viewBox="0 0 12 12"><circle cx="6" cy="6" r="5" fill="none" stroke="#ff8a00" stroke-width="1.6"/><path d="M6 3v3h2" stroke="#ff8a00" stroke-width="1.4" fill="none"/></svg>11 hours</div>
    <div class="divider"></div>
    <div class="pick">Top Insider's Pick</div>
    <div class="from">From USD $ <strong>128.61</strong></div>
    <div class="save"><s>$135.38</s> Save <span>$6.77</span></div>
    <a class="deal" href="#">VIEW DEAL</a>
  </article>

  <article class="card" style="top:1683px">
    <div class="photo" role="img" aria-label="Ornate palace facade beside a lake" style="background:linear-gradient(180deg,#e6d6b8,#c9a877 55%,#7b9bb3 75%,#4f7594)"></div>
    <svg class="fav" width="20" height="18" viewBox="0 0 20 18"><path d="M10 18 1.5 9.5A5 5 0 0 1 10 3a5 5 0 0 1 8.5 6.5z" fill="#e53935"/></svg>
    <h2>Nemo enim ipsam voluptem quia voluptas sitip</h2>
    <div class="stars"><b>★★★★☆</b>5042 Reviews</div>
    <div class="meta" style="top:113px"><svg width="9" height="12" viewBox="0 0 10 13"><path d="M5 0a5 5 0 0 1 5 5c0 4-5 8-5 8S0 9 0 5a5 5 0 0 1 5-5z" fill="#ff8a00"/></svg>London, United Kingdom</div>
    <div class="meta" style="top:137px"><svg width="12" height="12" viewBox="0 0 12 12"><circle cx="6" cy="6" r="5" fill="none" stroke="#ff8a00" stroke-width="1.6"/><path d="M6 3v3h2" stroke="#ff8a00" stroke-width="1.4" fill="none"/></svg>11 hours</div>
    <div class="divider"></div>
    <div class="pick">Top Insider's Pick</div>
    <div class="from">From USD $ <strong>128.61</strong></div>
    <div class="save"><s>$135.38</s> Save <span>$6.77</span></div>
    <a class="deal" href="#">VIEW DEAL</a>
  </article>

  <article class="card" style="top:1898px">
    <div class="photo" role="img" aria-label="Resort pavilion and pool at twilight" style="background:linear-gradient(180deg,#1f3f66,#4f6f94 40%,#b99466 65%,#2aa3c4)"></div>
    <svg class="fav" width="20" height="18" viewBox="0 0 20 18"><path d="M10 18 1.5 9.5A5 5 0 0 1 10 3a5 5 0 0 1 8.5 6.5z" fill="#e53935"/></svg>
    <h2>Nemo enim ipsam voluptem quia voluptas sitip</h2>
    <div class="stars"><b>★★★★☆</b>5042 Reviews</div>
    <div class="meta" style="top:113px"><svg width="9" height="12" viewBox="0 0 10 13"><path d="M5 0a5 5 0 0 1 5 5c0 4-5 8-5 8S0 9 0 5a5 5 0 0 1 5-5z" fill="#ff8a00"/></svg>London, United Kingdom</div>
    <div class="meta" style="top:137px"><svg width="12" height="12" viewBox="0 0 12 12"><circle cx="6" cy="6" r="5" fill="none" stroke="#ff8a00" stroke-width="1.6"/><path d="M6 3v3h2" stroke="#ff8a00" stroke-width="1.4" fill="none"/></svg>11 hours</div>
    <div class="divider"></div>
    <div class="pick">Top Insider's Pick</div>
    <div class="from">From USD $ <strong>128.61</strong></div>
    <div class="save"><s>$135.38</s> Save <span>$6.77</span></div>
    <a class="deal" href="#">VIEW DEAL</a>
  </article>

  <article class="card" style="top:2113px">
    <div class="photo" role="img" aria-label="Tropical resort lit up over water at dusk" style="background:linear-gradient(180deg,#2d4f8c,#6f8dbd 40%,#3a3a3a 60%,#2e6ea0)"></div>
    <svg class="fav" width="20" height="18" viewBox="0 0 20 18"><path d="M10 18 1.5 9.5A5 5 0 0 1 10 3a5 5 0 0 1 8.5 6.5z" fill="#e53935"/></svg>
    <h2>Nemo enim ipsam voluptem quia voluptas sitip</h2>
    <div class="stars"><b>★★★★☆</b>5042 Reviews</div>
    <div class="meta" style="top:113px"><svg width="9" height="12" viewBox="0 0 10 13"><path d="M5 0a5 5 0 0 1 5 5c0 4-5 8-5 8S0 9 0 5a5 5 0 0 1 5-5z" fill="#ff8a00"/></svg>London, United Kingdom</div>
    <div class="meta" style="top:137px"><svg width="12" height="12" viewBox="0 0 12 12"><circle cx="6" cy="6" r="5" fill="none" stroke="#ff8a00" stroke-width="1.6"/><path d="M6 3v3h2" stroke="#ff8a00" stroke-width="1.4" fill="none"/></svg>11 hours</div>
    <div class="divider"></div>
    <div class="pick">Top Insider's Pick</div>
    <div class="from">From USD $ <strong>128.61</strong></div>
    <div class="save"><s>$135.38</s> Save <span>$6.77</span></div>
    <a class="deal" href="#">VIEW DEAL</a>
  </article>

  <nav class="pager"><span>Prev</span><span class="on">1</span><span>2</span><span>3</span><span>4</span><span>5</span><span>6</span><span>...</span><span>22</span><span>Next</span></nav>

  <section class="panel" style="top:2430px;height:363px">
    <h2>Top Destinations</h2>
    <div class="arrows"><span><svg width="8" height="10"><path d="M6 1 2 5l4 4" stroke="#fff" stroke-width="2" fill="none"/></svg></span><span><svg width="8" height="10"><path d="M2 1l4 4-4 4" stroke="#fff" stroke-width="2" fill="none"/></svg></span></div>
    <div class="dest" style="left:28px">
      <div class="photo" role="img" aria-label="Canal city at sunset" style="background:linear-gradient(180deg,#5b8ec4,#e0a96d 55%,#2d5d7c)"></div>
      <span class="name">Hotels London</span><span class="count">10809 Hotels</span><span class="price">$175.19</span>
    </div>
    <div class="dest" style="left:268px">
      <div class="photo" role="img" aria-label="Coastal town with turquoise sea" style="background:linear-gradient(180deg,#4aa3d8,#e6e1d6 50%,#1fa6b8)"></div>
      <span class="name">Hotels London</span><span class="count">10809 Hotels</span><span class="price">$175.19</span>
    </div>
    <div class="dest" style="left:507px">
      <div class="photo" role="img" aria-label="Historic lakeside buildings" style="background:linear-gradient(180deg,#4f86c2,#d8a562 55%,#3b6d8a)"></div>
      <span class="name">Hotels London</span><span class="count">10809 Hotels</span><span class="price">$175.19</span>
    </div>
  </section>

  <section class="panel" style="top:2839px;height:334px">
    <h2 style="left:38px;top:30px;font-size:29px">More Things to Do in London</h2>
    <ul class="things">
      <li>Airport &amp; Ground Transfers</li><li>Attraction Tickets</li><li>Bar, Club &amp; Pub Tours</li><li>Bike &amp; Mountain Bike Tours</li><li>City Tours</li><li>Cultural Tours</li><li>Day Cruises</li>
      <li>Day Trips</li><li>Dinner Packages</li><li>Food Tours</li><li>Full-day Tours</li><li>Half-day Tours</li><li>Hop-on Hop-off Tours</li><li>Movie &amp; TV Tours</li>
      <li>Night Tours</li><li>Private Transfers</li><li>Rail Tours</li><li>Sightseeing &amp; City Passes</li><li>Theater, Shows &amp; Musicals</li><li>Walking Tours</li><li style="visibility:hidden">-</li>
    </ul>
  </section>
</main>

<footer class="site-footer">
  <div class="foot-brand">WAYFARER DESK</div>
  <p class="foot-about">At vero eos et accusamus et iusto odio dignissi mos ducimus qui blanditiis.</p>
  <div class="socials">
    <span style="background:#3aa757"></span><span style="background:#3b5998"></span><span style="background:#1da1f2"></span><span style="background:#dd4b39"></span><span style="background:#0e76a8"></span><span style="background:#4a7ab8"></span><span style="background:#e62117"></span><span style="background:#c8232c"></span>
  </div>
  <div class="foot-col" style="left:467px"><h4>Information</h4><ul><li>About Us</li><li>Careers</li><li>Privacy &amp; Security</li><li>Site Map</li><li>Terms of Use</li><li>Blog</li></ul></div>
  <div class="foot-col" style="left:670px"><h4>Customer Care</h4><ul><li>Help Center</li><li>Privacy Policy</li><li>Low Price Guarantee</li><li>Group Services</li></ul></div>
  <div class="foot-col" style="left:920px"><h4>Resources</h4><ul><li>Work with Wayfarer Desk</li><li>Supplier Sign-up</li><li>Distribution Programs</li><li>Travel Agents</li></ul></div>
  <p class="copyright">Copyright © 2017, Wayfarer Desk - All Rights Reserved.</p>
</footer>

</body>
</html>
```